Consulting firm needs a professional letterhead design

We need a professional letterhead design which is simple but unique. It should carry attributes of the latest designs in the market suitable for professional environmental consultancies.

- The logo is attached for you to USE.
- Our preferred color scheme is that shown in the logo.
- Letterhead text color is your choice to make.
- Logo to the left and text to the right plus slogan/tagline is desirable for this letterhead.

Use any address etc. of your choice in the letterhead.

Target Market(s)

Consulting firms and government agencies

Industry/Entity Type

Environmental Consultant

Colors
acd037
fece3e
85cae6
3277b5

Requirements
Must have
• Logo supplied and color scheme must be used.
Nice to have
• Nexa font is used in the Logo, so it would ne nice to have nexa font in the letterhead too.

```html
<!DOCTYPE html>
<html lang="en">
<head>
<meta charset="utf-8">
<title>Terravista Letterhead</title>
<link href="https://fonts.googleapis.com/css2?family=Questrial&family=Parisienne&display=swap" rel="stylesheet">
<style>
  :root {
    --brand-blue: #17809f;
    --brand-orange: #f28a21;
    --brand-green: #1ba04b;
    --ink-navy: #2c3550;
    --ink-body: #4f4f4f;
    --ink-signature: #1b86a8;
    --paper: #ffffff;
  }
  * { margin: 0; padding: 0; box-sizing: border-box; }
  html, body { width: 949px; height: 1200px; overflow: hidden; background: var(--paper); }
  body { font-family: "Questrial", sans-serif; color: var(--ink-body); }

  .letterhead { position: relative; width: 949px; height: 1200px; }

  .brand { position: absolute; left: 56px; top: 150px; width: 262px; }
  .brand-mark { display: flex; align-items: center; gap: 9px; }
  .brand-dot { width: 18px; height: 18px; border-radius: 50%; background: var(--brand-blue); flex: none; }
  .brand-name { font-size: 29px; letter-spacing: 2px; color: var(--ink-navy); line-height: 1; }
  .brand-tagline { display: block; font-size: 12.5px; color: var(--ink-navy); margin-top: 3px; white-space: nowrap; }

  .postal-address {
    position: absolute; right: 316px; top: 131px;
    text-align: right; font-size: 14.5px; line-height: 19px; font-style: normal; color: var(--ink-body);
  }
  .contact-divider {
    position: absolute; left: 651px; top: 115px; width: 1.5px; height: 57px; background: var(--brand-orange);
  }
  .contact-list {
    position: absolute; left: 668px; top: 109px; list-style: none;
    font-size: 14.5px; line-height: 21px;
  }
  .contact-list li { display: flex; align-items: center; gap: 8px; white-space: nowrap; }
  .contact-list svg { width: 14px; height: 14px; flex: none; }

  .tricolor-rule { position: absolute; left: 56px; right: 56px; top: 227px; height: 3px; display: flex; }
  .tricolor-rule span, .tricolor-band span { flex: 1; }
  .tricolor-band { position: absolute; left: 0; right: 0; bottom: 0; height: 20px; display: flex; }
  .blue { background: var(--brand-blue); }
  .orange { background: var(--brand-orange); }
  .green { background: var(--brand-green); }

  .recipient { position: absolute; left: 56px; top: 330px; font-size: 14px; line-height: 20px; }

  .letter-body {
    position: absolute; left: 56px; right: 56px; top: 434px;
    font-size: 13.9px; line-height: 20px; text-align: justify;
  }
  .letter-body p + p { margin-top: 25px; }

  .sign-off { position: absolute; left: 56px; top: 821px; }
  .sign-label { font-size: 14px; }
  .sign-name { font-family: "Parisienne", cursive; font-size: 24px; color: var(--ink-signature); margin-top: 2px; }
</style>
</head>
<body>
<main class="letterhead">
  <header class="masthead">
    <div class="brand">
      <div class="brand-mark">
        <span class="brand-dot"></span>
        <span class="brand-name">TERRAVISTA</span>
      </div>
      <span class="brand-tagline">Bridging research and policy choices</span>
    </div>

    <address class="postal-address">45 Riverside Lane Kasai,<br>Suite 3, 40210</address>
    <div class="contact-divider"></div>
    <ul class="contact-list">
      <li>
        <svg viewBox="0 0 16 16"><path d="M3.5 1.5l2.5 0.5 1 3-1.6 1.4a9 9 0 0 0 4.2 4.2L11 9l3 1 .5 2.5-1.8 1.8C7 14 2 9 1.7 3.3z" fill="var(--brand-blue)"/></svg>
        +243 800 555 019
      </li>
      <li>
        <svg viewBox="0 0 16 16"><rect x="1.5" y="3.5" width="13" height="9" fill="none" stroke="var(--brand-blue)" stroke-width="1.2"/><path d="M1.5 3.5L8 9l6.5-5.5" fill="none" stroke="var(--brand-blue)" stroke-width="1.2"/></svg>
        contact@terravista-advisory.com
      </li>
      <li>
        <svg viewBox="0 0 16 16"><g fill="none" stroke="var(--brand-blue)" stroke-width="1.1"><circle cx="8" cy="8" r="6.5"/><ellipse cx="8" cy="8" rx="3" ry="6.5"/><path d="M1.5 8h13M2.5 4.8h11M2.5 11.2h11"/></g></svg>
        www.terravista-advisory.com
      </li>
    </ul>
  </header>

  <div class="tricolor-rule"><span class="blue"></span><span class="orange"></span><span class="green"></span></div>

  <section class="recipient">
    Mr/s<br>First Name and Last Name<br>Company Name<br>Address
  </section>

  <section class="letter-body">
    <p>Contrary to popular belief, Lorem Ipsum is not simply random text. It has roots in a piece of classical Latin literature from 45 BC, making it over 2000 years old. A Latin scholar at a small college in the hills looked up one of the more obscure Latin words, consectetur, from a Lorem Ipsum passage, and going through the cites of the word in classical literature, discovered the undoubtable source. Lorem Ipsum comes from sections 1.10.32 and 1.10.33 of an old treatise on the extremes of good and evil, written in 45 BC. This book is a study of the theory of ethics, very popular during the Renaissance. The first line of Lorem Ipsum, "Lorem ipsum dolor sit amet.</p>
    <p>he standard chunk of Lorem Ipsum used since the 1500s is reproduced below for those interested. Sections 1.10.32 and 1.10.33 from the same classical treatise are also reproduced in their exact original form, accompanied by English versions from an early translation of the last century. Lorem ipsum dolor sit amet, consectetur adipiscing elit, sed do eiusmod tempor incididunt ut labore et dolore magna aliqua. Ut enim ad minim veniam, quis nostrud exercitation ullamco laboris nisi ut aliquip ex ea commodo consequat.</p>
    <p>It is a long established fact that a reader will be distracted by the readable content of a page when looking at its layout. The point of using Lorem Ipsum is that it has a more-or-less normal distribution of letters, as opposed to using 'Content here, content here', making it look like readable English. Many desktop publishing packages and web page editors now .</p>
  </section>

  <section class="sign-off">
    <p class="sign-label">Signature</p>
    <p class="sign-name">Dalen Morrow</p>
  </section>

  <footer class="tricolor-band"><span class="blue"></span><span class="orange"></span><span class="green"></span></footer>
</main>
</body>
</html>
```